Security Warning Sign

We have an existing sign that needs an update. I have attached a picture of the current square sign. We need to maintain the same wording. It needs to be professional and appropriate to attach to our customers fence. Also attached is a copy of our building sign which may lend some inspiration and hopefully the ai format will assist. The final sign will be 600mm x 600mmOur website is www.halvorngate.com.au

```html
<!DOCTYPE html>
<html lang="en">
<head>
<meta charset="utf-8">
<title>Halvorngate Security Services – Surveillance Warning Sign</title>
<link rel="stylesheet" href="https://fonts.googleapis.com/css2?family=Anton&family=Archivo+Black&display=swap">
<style>
  :root {
    --brand-orange: #F28420;
    --ink: #262626;
    --paper: #FFFFFF;
    --camera-light: #E6E8EA;
    --camera-dark: #1A1C20;
  }
  html, body {
    margin: 0;
    padding: 0;
    width: 1200px;
    height: 1200px;
    overflow: hidden;
    background: var(--paper);
  }
  .sign {
    display: block;
    width: 1200px;
    height: 1200px;
  }
  .band { fill: var(--brand-orange); }
  .brand-dot { fill: var(--brand-orange); }
  .brand-name {
    font-family: "Archivo Black", sans-serif;
    font-size: 42px;
    fill: var(--ink);
  }
  .contact-phone {
    font-family: "Archivo Black", sans-serif;
    font-size: 92px;
    fill: var(--ink);
  }
  .contact-web {
    font-family: "Anton", sans-serif;
    font-size: 44px;
    fill: var(--ink);
  }
  .phone-icon { fill: var(--ink); }
  .phone-waves { fill: none; stroke: var(--ink); stroke-width: 6; stroke-linecap: round; }
  .headline {
    font-family: "Anton", sans-serif;
    font-size: 204px;
    fill: var(--paper);
  }
  .notice {
    font-family: "Archivo Black", sans-serif;
    font-size: 122px;
    fill: var(--ink);
  }
  .footer-line {
    font-family: "Archivo Black", sans-serif;
    font-size: 172px;
    fill: var(--paper);
  }
</style>
</head>
<body>
<svg class="sign" viewBox="0 0 1200 1200" xmlns="http://www.w3.org/2000/svg">
  <defs>
    <radialGradient id="camera-tone" cx="0.55" cy="0.6" r="0.6">
      <stop offset="0" stop-color="var(--camera-dark)"/>
      <stop offset="0.45" stop-color="#3A3D44"/>
      <stop offset="0.75" stop-color="#CFD2D6"/>
      <stop offset="1" stop-color="var(--camera-light)"/>
    </radialGradient>
  </defs>

  <!-- Brand block -->
  <g class="brand">
    <circle class="brand-dot" cx="110" cy="104" r="70"/>
    <text class="brand-name" x="211" y="78" textLength="285" lengthAdjust="spacingAndGlyphs">HALVORNGATE</text>
    <text class="brand-name" x="211" y="122">SECURITY</text>
    <text class="brand-name" x="211" y="165">SERVICES</text>
  </g>

  <!-- Contact block -->
  <g class="contact">
    <path class="phone-icon" d="M546 32c6-5 12-4 16 2l14 20c4 6 3 12-3 16l-9 6c-3 2-3 5-1 9 7 13 16 22 29 29 4 2 7 2 9-1l6-9c4-6 10-7 16-3l2 2-12 12 -8 8c-6 5-13 6-20 3-28-12-48-32-60-60-3-7-2-14 3-20z"/>
    <path class="phone-waves" d="M572 46a18 18 0 0 1 18 18 M572 32a32 32 0 0 1 32 32"/>
    <text class="contact-phone" x="615" y="93" textLength="565" lengthAdjust="spacingAndGlyphs">1300 555 014</text>
    <text class="contact-web" x="539" y="169" textLength="647" lengthAdjust="spacingAndGlyphs">WWW.HALVORNGATE.COM.AU</text>
  </g>

  <!-- Warning band -->
  <rect class="band" x="0" y="207" width="1200" height="218"/>
  <text class="headline" x="71" y="397" textLength="1045" lengthAdjust="spacingAndGlyphs">WARNING</text>

  <!-- Camera image area -->
  <rect x="829" y="425" width="371" height="311" rx="150" fill="url(#camera-tone)" role="img" aria-label="Photo of a white dome security camera with infrared LEDs"/>

  <!-- Notice text -->
  <g class="notice-block">
    <text class="notice" x="51" y="551" textLength="637" lengthAdjust="spacingAndGlyphs">ELECTRONIC</text>
    <text class="notice" x="51" y="693" textLength="768" lengthAdjust="spacingAndGlyphs">SURVEILLANCE</text>
    <text class="notice" x="45" y="834" textLength="863" lengthAdjust="spacingAndGlyphs">AND RECORDING</text>
    <text class="notice" x="51" y="974" textLength="1015" lengthAdjust="spacingAndGlyphs">DEVICES INSTALLED</text>
  </g>

  <!-- Footer band -->
  <rect class="band" x="0" y="997" width="1200" height="203"/>
  <text class="footer-line" x="160" y="1143" textLength="907" lengthAdjust="spacingAndGlyphs">IN THE AREA</text>
</svg>
</body>
</html>
```